Premium Wagyu Smallgoods Packaging Design (A5)

Hi there,
We are Ember Ridge Wagyu; a wagyu beef company based in Christchurch, New Zealand. We are needing new packaging for our new line of wagyu smallgoods (salami, braesola, fina seca etc.).
About us: Ember Ridge Wagyu began in 2015 and has since been tirelessly rearing stock to the quality and levels needed to supply the best restaurants and consumers. We combine the origin of Japanese breeding genetics and 200 year old techniques with New Zealand’s grass, grain, water and air.
Website:
https://emberridge-example.co.nz/
Brand Guidelines:
https://brandpages-example.net/view/emberridgebrandguide/home?authuser=0
The smallgoods packaging designs should have consistent branding, with only the product names and colours changing across the designs. The placement of the gold foil needs to be consistent across all the designs.
The packaging dimensions are 17 x 24 cm.
The required components that need to be on the FRONT of the packaging are:
- Our logo
- The product weight
- The product name
The required components that need to be on the BACK of the packaging are:
- Proudly Farmed in New Zealand
- Keep chilled at or below 4°c
- 42 Tannery Lane, Halsworth, Christchurch, New Zealand
- Spaceholder text (we will include some information about the brand)
- Gold medals/badges to emphasize our main selling points
Attached are some drafts as well as our logos. If you need additional imagery or further questions please don't hesitate to contact us at the following emails below:
contact@emberridge-example.co.nz
petra@emberridge-example.co.nz

```html
<!DOCTYPE html>
<html lang="en">
<head>
<meta charset="utf-8">
<title>Ember Ridge Wagyu — Smallgoods Range</title>
<link rel="stylesheet" href="https://fonts.googleapis.com/css2?family=Cinzel:wght@400&family=Montserrat:wght@600;700;800&family=Roboto+Condensed:wght@400;700&display=swap">
<style>
  :root {
    --page: #ffffff;
    --pack: #15151d;
    --pack-light: #2a2a35;
    --white: #ffffff;
    --window: #f5f5f5;
    --gold: #c9a25a;
    --ink: #1b1b1b;
    --link-red: #c4161c;
    --braesola-a: #5a0e0e;
    --braesola-b: #c3161f;
    --salami-a: #36093a;
    --salami-b: #911f88;
    --finaseca-a: #b4511c;
    --finaseca-b: #f6b215;
  }
  * { box-sizing: border-box; margin: 0; padding: 0; }
  html, body { width: 1200px; height: 873px; overflow: hidden; background: var(--page); }
  .range { position: relative; width: 1200px; height: 873px; }

  .pack {
    position: absolute; top: 174px; width: 372px; height: 528px;
    background: radial-gradient(ellipse 70% 45% at 55% 30%, var(--pack-light), var(--pack) 75%);
    box-shadow: 0 3px 8px rgba(0,0,0,.25);
  }
  .pack--braesola { left: 31px; }
  .pack--salami { left: 416px; }
  .pack--fina-seca { left: 800px; }

  .hang-slot {
    position: absolute; left: 157px; top: 31px; width: 56px; height: 14px;
    background: var(--white); border-radius: 7px;
  }
  .hang-slot::before {
    content: ""; position: absolute; left: 22px; top: -7px; width: 12px; height: 12px;
    background: var(--white); border-radius: 50%;
  }

  .brand {
    position: absolute; left: 0; right: 0; top: 82px; text-align: center;
    font-family: "Montserrat", sans-serif; font-weight: 800; color: var(--white);
    font-size: 44px; line-height: 52px; letter-spacing: 0.02em;
  }

  .window {
    position: absolute; left: 57px; top: 210px; width: 269px; height: 169px;
    background: linear-gradient(100deg, var(--white) 48%, var(--window) 48%);
    border: 1.5px solid var(--gold);
  }

  .label {
    position: absolute; left: 57px; top: 384px; width: 268px; height: 120px;
    background: var(--white); border: 3px dotted var(--pack);
    outline: 2px solid var(--white); outline-offset: -5px;
  }
  .label__name {
    position: absolute; left: 11px; top: 19px; width: 240px; height: 28px;
    font-family: "Cinzel", serif; font-weight: 400; font-size: 25px; line-height: 28px;
    color: var(--white); text-align: center; letter-spacing: 0.08em;
  }
  .pack--braesola .label__name { background: linear-gradient(90deg, var(--braesola-a), var(--braesola-b)); }
  .pack--salami .label__name { background: linear-gradient(90deg, var(--salami-a), var(--salami-b)); }
  .pack--fina-seca .label__name { background: linear-gradient(90deg, var(--finaseca-a), var(--finaseca-b)); }

  .label__tagline {
    position: absolute; left: 11px; width: 240px; top: 51px; padding-bottom: 2px;
    font-family: "Roboto Condensed", sans-serif; font-weight: 700; font-size: 5px;
    letter-spacing: 0.06em; color: var(--ink); text-align: left; white-space: nowrap;
  }
  .label__tagline-rule { position: absolute; left: 11px; top: 60px; width: 190px; height: 0.6px; background: var(--ink); }
  .weight {
    position: absolute; left: 15px; top: 70px; font-family: "Roboto Condensed", sans-serif;
    color: var(--ink); line-height: 1;
  }
  .weight__label { font-size: 5.5px; }
  .weight__value { font-size: 11.5px; font-weight: 700; margin: 1px 0; }
  .weight__note { font-size: 4.5px; }
  .divider { position: absolute; left: 63px; top: 64px; width: 0.8px; height: 36px; background: var(--ink); }
  .farmed {
    position: absolute; left: 67px; width: 128px; top: 69px; text-align: center;
    font-family: "Montserrat", sans-serif; font-weight: 600; font-size: 5px;
    letter-spacing: 0.1em; line-height: 1.1; color: var(--ink);
  }
  .rule { position: absolute; left: 67px; top: 83px; width: 128px; height: 0.6px; background: var(--ink); }
  .web {
    position: absolute; left: 67px; width: 128px; top: 91px; text-align: center;
    font-family: "Montserrat", sans-serif; font-weight: 700; font-size: 5px;
    letter-spacing: 0.12em; color: var(--link-red);
  }
  .seal {
    position: absolute; left: 205px; top: 58px; width: 40px; height: 40px;
    border-radius: 50%; border: 1.2px solid var(--gold);
  }
</style>
</head>
<body>
<main class="range">

  <section class="pack pack--braesola">
    <div class="hang-slot"></div>
    <h1 class="brand">EMBER<br>RIDGE</h1>
    <div class="window"></div>
    <div class="label">
      <h2 class="label__name">BRAESOLA</h2>
      <p class="label__tagline">A NEW ARTISAN DELICACY, OUR WAGYU FINA SECA IS FINELY SLICED AND DRY-CURED</p>
      <div class="label__tagline-rule"></div>
      <div class="weight"><div class="weight__label">Net Weight</div><div class="weight__value">150g</div><div class="weight__note">(Approx)</div></div>
      <div class="divider"></div>
      <p class="farmed">PROUDLY FARMED<br>IN NEW ZEALAND</p>
      <div class="rule"></div>
      <p class="web">EMBERRIDGE-EXAMPLE.CO.NZ</p>
      <div class="seal" role="img" aria-label="Grain fed wagyu seal"></div>
    </div>
  </section>

  <section class="pack pack--salami">
    <div class="hang-slot"></div>
    <h1 class="brand">EMBER<br>RIDGE</h1>
    <div class="window"></div>
    <div class="label">
      <h2 class="label__name">SALAMI</h2>
      <p class="label__tagline">A NEW ARTISAN DELICACY, OUR WAGYU FINA SECA IS FINELY SLICED AND DRY-CURED</p>
      <div class="label__tagline-rule"></div>
      <div class="weight"><div class="weight__label">Net Weight</div><div class="weight__value">150g</div><div class="weight__note">(Approx)</div></div>
      <div class="divider"></div>
      <p class="farmed">PROUDLY FARMED<br>IN NEW ZEALAND</p>
      <div class="rule"></div>
      <p class="web">EMBERRIDGE-EXAMPLE.CO.NZ</p>
      <div class="seal" role="img" aria-label="Grain fed wagyu seal"></div>
    </div>
  </section>

  <section class="pack pack--fina-seca">
    <div class="hang-slot"></div>
    <h1 class="brand">EMBER<br>RIDGE</h1>
    <div class="window"></div>
    <div class="label">
      <h2 class="label__name">FINA SECA</h2>
      <p class="label__tagline">A NEW ARTISAN DELICACY, OUR WAGYU FINA SECA IS FINELY SLICED AND DRY-CURED</p>
      <div class="label__tagline-rule"></div>
      <div class="weight"><div class="weight__label">Net Weight</div><div class="weight__value">150g</div><div class="weight__note">(Approx)</div></div>
      <div class="divider"></div>
      <p class="farmed">PROUDLY FARMED<br>IN NEW ZEALAND</p>
      <div class="rule"></div>
      <p class="web">EMBERRIDGE-EXAMPLE.CO.NZ</p>
      <div class="seal" role="img" aria-label="Grain fed wagyu seal"></div>
    </div>
  </section>

</main>
</body>
</html>
```